20 year old business card needs re-design

We need to redesign our corporate business card look. We need something that appears more modern, eye catchy but professional.

Target Market(s)

manufacturing industry

Industry/Entity Type

Manufacturer

Contact Information for Business Card

One side can have the logo. Other side can have contact information.

Font styles to use
Serif

Colors
3277b5
33b8a4
ffffff

Requirements
Must have
• Eye catchy - need to standout from the crowd. company logo cannot change. Full name, job title, phone number and email address.
Should not have
• Fax, business address is not necessary.

```html
<!DOCTYPE html>
<html lang="en">
<head>
<meta charset="utf-8">
<title>Norvale Industries – Business Card</title>
<link rel="stylesheet" href="https://fonts.googleapis.com/css2?family=Open+Sans:wght@400;700;800&display=swap">
<style>
  :root {
    --backdrop: #2b2b2b;
    --card: #f7f7f7;
    --brand-blue: #1e4f98;
    --ink: #1b1b1b;
    --ink-soft: #2e2e2e;
    --white: #ffffff;
  }
  * { box-sizing: border-box; margin: 0; padding: 0; }
  html, body {
    width: 1200px; height: 997px; overflow: hidden;
    background: var(--backdrop);
    font-family: "Open Sans", Arial, sans-serif;
  }
  .sheet {
    width: 1200px; height: 997px;
    display: flex; flex-direction: column; align-items: center; justify-content: center;
    gap: 60px;
  }
  .card {
    position: relative;
    width: 640px; height: 366px;
    background: var(--card);
    border-radius: 4px;
    overflow: hidden;
    box-shadow: 0 10px 30px rgba(0,0,0,.45);
  }
  /* Logo stand-in */
  .brand {
    position: absolute; left: 0; right: 0;
    display: flex; align-items: center; justify-content: center; gap: 14px;
    font-weight: 800; color: var(--brand-blue);
    letter-spacing: .02em;
  }
  .brand-mark { background: var(--brand-blue); }
  .card--front .brand { top: 150px; font-size: 40px; }
  .card--front .brand-mark { width: 34px; height: 34px; }
  .card--back .brand { top: 62px; font-size: 32px; }
  .card--back .brand-mark { width: 28px; height: 28px; }

  /* Contact block */
  .contact {
    position: absolute; right: 56px; top: 150px;
    list-style: none; text-align: right;
    font-size: 13px; line-height: 26px; color: var(--ink-soft);
  }
  .contact-tab {
    position: absolute; right: 0; top: 148px;
    width: 34px; height: 82px;
    background: var(--brand-blue);
    border-radius: 8px 0 0 8px;
    display: flex; flex-direction: column; align-items: center; justify-content: space-around;
    padding: 6px 0;
  }
  .contact-tab svg { width: 14px; height: 14px; fill: var(--white); }

  /* Holder */
  .holder-tab {
    position: absolute; left: 0; top: 246px;
    width: 12px; height: 54px;
    background: var(--brand-blue);
    border-radius: 0 6px 6px 0;
  }
  .holder {
    position: absolute; left: 28px; top: 248px;
  }
  .holder-name {
    font-size: 18px; font-weight: 700; color: var(--brand-blue); letter-spacing: .01em;
  }
  .holder-title {
    font-size: 12px; font-weight: 700; color: var(--ink-soft); margin-top: 2px;
  }

  /* Web band */
  .web-band {
    position: absolute; left: 0; right: 0; top: 312px;
    height: 28px;
    background: var(--brand-blue);
    color: var(--white);
    font-size: 16px; font-weight: 700; letter-spacing: .04em;
    display: flex; align-items: center; justify-content: flex-end;
    padding-right: 130px;
  }
</style>
</head>
<body>
<main class="sheet">

  <section class="card card--front" aria-label="Card front">
    <div class="brand"><span class="brand-mark"></span><span class="brand-name">NORVALE INDUSTRIES</span></div>
  </section>

  <section class="card card--back" aria-label="Card back">
    <div class="brand"><span class="brand-mark"></span><span class="brand-name">NORVALE INDUSTRIES</span></div>

    <ul class="contact">
      <li>+61 491 570 156</li>
      <li>info@norvale.com.au</li>
      <li>Riverton QLD 4101</li>
    </ul>
    <div class="contact-tab" aria-hidden="true">
      <svg viewBox="0 0 24 24"><path d="M6.6 10.8a15.1 15.1 0 0 0 6.6 6.6l2.2-2.2a1 1 0 0 1 1-.25 11.4 11.4 0 0 0 3.6.57 1 1 0 0 1 1 1V20a1 1 0 0 1-1 1A17 17 0 0 1 3 4a1 1 0 0 1 1-1h3.5a1 1 0 0 1 1 1c0 1.25.2 2.45.57 3.57a1 1 0 0 1-.25 1z"/></svg>
      <svg viewBox="0 0 24 24"><path d="M3 5h18a1 1 0 0 1 1 1v12a1 1 0 0 1-1 1H3a1 1 0 0 1-1-1V6a1 1 0 0 1 1-1zm9 7.5L20 7H4z"/></svg>
      <svg viewBox="0 0 24 24"><path d="M12 2a7 7 0 0 0-7 7c0 5.2 7 13 7 13s7-7.8 7-13a7 7 0 0 0-7-7zm0 9.5A2.5 2.5 0 1 1 12 6.5a2.5 2.5 0 0 1 0 5z"/></svg>
    </div>

    <div class="holder-tab" aria-hidden="true"></div>
    <div class="holder">
      <p class="holder-name">CLARA WHITFIELD</p>
      <p class="holder-title">FOUNDER &amp; CEO</p>
    </div>

    <div class="web-band">WWW.NORVALEINDUSTRIES.COM</div>
  </section>

</main>
</body>
</html>
```